Website Design for a "Talent Recruitment Agency"

We are looking for a website design for the website of our "Talent Recruitment Agency"; which is called "Crestline Circle".
Our recruitment website "Crestline Circle" will be focusing on: "Crestline Circle: Bridging People & Employers in Switzerland"; which means our target audience is two-folded:
(i) TALENT - that is currently residing in- or outside of Switzerland, and is open for and interested in the "Swiss Job Market".
(ii) COMPANIES - that are looking for talent for specific job vacancies in Switzerland.
With our "Crestline Circle" approach we inted to focus on Membership & Partnership:
(a)"Membership"(TALENT)
and
(b)"Partnership"(COMPANIES)
Some of the competitor sites we like are:
• www.brimlo42.dk
• www.qazet.ch
• www.plovik.ch/en
A sitemap example of our website is attached.
Also attached is a "Crestline Circle" logo in .eps format and one in .jpeg format.
We very much look forward to receive your creative ideas.
Best regards,
Crestline Circle
Crestline Circle: Bridging People & Employers in Switzerland.
Website: crestlinecircle.ch - Twitter: CrestlineCircleCH
Target Market(s)
(i) TALENT (with around 0-10 years of working experience), currently residing in- or outside of Switzerland, but eligible to work in Switzerland.
(ii) COMPANIES (national or international) that are based in Switzerland.
Industry/Entity Type
Recruitment

```html
<!DOCTYPE html>
<html lang="en">
<head>
<meta charset="utf-8">
<title>Crestline Circle – Available Jobs</title>
<link href="https://fonts.googleapis.com/css2?family=Ubuntu:wght@400;500&display=swap" rel="stylesheet">
<style>
  :root {
    --navy-top: #0c3d63;
    --navy: #08304f;
    --navy-deep: #04233b;
    --navy-bottom: #062a44;
    --panel-blue: #0677be;
    --row-hover: #05649f;
    --row-line: #2a8fd0;
    --table-head: #01264a;
    --orange: #f37321;
    --orange-dark: #d9611a;
    --brand-blue: #1a8ad8;
    --white: #ffffff;
    --ink-dark: #0c2a44;
    --link-dark: #7a2d05;
  }
  * { box-sizing: border-box; margin: 0; padding: 0; }
  html, body { width: 959px; height: 1200px; overflow: hidden; }
  body {
    position: relative;
    font-family: "Ubuntu", sans-serif;
    color: var(--white);
    background: linear-gradient(to bottom, #0e4a73 0px, var(--navy) 404px, var(--navy-deep) 404px, var(--navy-deep) 523px, var(--navy-bottom) 523px);
  }
  .site-header { position: absolute; left: 0; top: 0; width: 959px; height: 130px; }
  .brand { position: absolute; left: 38px; top: 30px; display: flex; align-items: center; gap: 10px; }
  .brand-mark { width: 34px; height: 34px; border-radius: 50%; background: var(--orange); }
  .brand-name { font-size: 38px; font-weight: 500; color: var(--orange); line-height: 1; }
  .brand-tagline { position: absolute; left: 82px; top: 81px; font-size: 11.5px; color: var(--white); }
  .languages { position: absolute; left: 786px; top: 57px; display: flex; gap: 15px; }
  .languages svg { width: 15px; height: 10px; display: block; }
  .main-nav { position: absolute; top: 79px; right: 68px; display: flex; gap: 16px; font-size: 11px; }
  .main-nav a { color: var(--white); text-decoration: none; }
  .main-nav a.is-active { color: var(--orange); }

  .page-banner { position: absolute; left: 38px; top: 133px; width: 884px; height: 145px; overflow: hidden; background: linear-gradient(to right, var(--orange-dark), var(--orange) 60%, #f07a2c); }
  .banner-photo { position: absolute; left: 0; top: 0; width: 228px; height: 145px; background: linear-gradient(135deg, #a49a90, #4f4842 55%, #2a2522); clip-path: polygon(0 0, 100% 0, 82% 100%, 0 100%); }
  .banner-title { position: absolute; left: 283px; top: 36px; color: #111; font-size: 28px; font-weight: 400; letter-spacing: .5px; }
  .banner-sub { position: absolute; left: 283px; top: 69px; font-size: 21px; color: var(--white); }

  .jobs-panel { position: absolute; left: 38px; top: 278px; width: 884px; height: 602px; background: var(--panel-blue); }
  .table-controls { position: absolute; left: 38px; top: 22px; width: 808px; font-size: 12.5px; display: flex; justify-content: space-between; align-items: center; }
  .entries-select { display: inline-block; width: 34px; height: 13px; background: var(--white); color: #000; font-size: 11px; line-height: 13px; padding-left: 2px; vertical-align: middle; margin: 0 4px; position: relative; }
  .entries-select::after { content: ""; position: absolute; right: 3px; top: 4px; border: 4px solid transparent; border-top: 5px solid #000; }
  .search-field { display: inline-block; width: 150px; height: 14px; background: var(--white); vertical-align: middle; margin-left: 10px; }
  .jobs-table { position: absolute; left: 37px; top: 45px; width: 848px; border-collapse: collapse; font-size: 12.5px; text-align: center; }
  .jobs-table th { background: var(--table-head); height: 29px; font-weight: 400; font-size: 12.5px; }
  .jobs-table td { height: 45px; border-bottom: 1px solid var(--row-line); }
  .jobs-table tr.is-hovered td { background: var(--row-hover); }
  .table-footer { position: absolute; left: 40px; top: 595px; }
  .table-info { position: absolute; left: 40px; top: 574px; font-size: 12.5px; color: var(--ink-dark); }
  .pagination { position: absolute; right: 40px; top: 574px; font-size: 12.5px; color: var(--ink-dark); display: flex; gap: 14px; }

  .site-footer-panel { position: absolute; left: 38px; top: 880px; width: 885px; height: 244px; background: var(--orange); }
  .footer-col { position: absolute; top: 36px; font-size: 12.5px; line-height: 16px; }
  .footer-col h2 { font-size: 16.5px; font-weight: 400; margin-bottom: 12px; }
  .footer-col p { margin-bottom: 16px; }
  .footer-col .more { position: absolute; font-style: italic; color: var(--link-dark); font-size: 12.5px; }
  .col-about { left: 39px; width: 285px; }
  .col-jobs { left: 376px; width: 215px; }
  .col-news { left: 621px; width: 240px; }
  .footer-divider { position: absolute; left: 348px; top: 36px; width: 3px; height: 180px; background: radial-gradient(circle, #fff 1.2px, transparent 1.6px) 0 0 / 3px 10px repeat-y; }

  .site-bottom { position: absolute; left: 38px; top: 1136px; font-size: 10.5px; line-height: 14px; }
  .social-links { position: absolute; left: 622px; top: 1133px; display: flex; gap: 8px; }
  .social-links span { width: 30px; height: 30px; border-radius: 3px; display: block; }
  .footer-brand { position: absolute; left: 808px; top: 1135px; display: flex; align-items: center; gap: 6px; }
  .footer-brand .brand-mark { width: 18px; height: 18px; }
  .footer-brand span.name { font-size: 14px; font-weight: 500; color: var(--orange); line-height: 14px; width: 100px; }
</style>
</head>
<body>
  <header class="site-header">
    <div class="brand"><span class="brand-mark"></span><span class="brand-name">Crestline Circle</span></div>
    <div class="brand-tagline">Crestline Circle: Bridging People &amp; Employers in Switzerland</div>
    <div class="languages">
      <svg viewBox="0 0 15 10" aria-label="English"><rect width="15" height="10" fill="#1f3c8a"/><path d="M0 0L15 10M15 0L0 10" stroke="#fff" stroke-width="2"/><path d="M7.5 0V10M0 5H15" stroke="#fff" stroke-width="3"/><path d="M7.5 0V10M0 5H15" stroke="#c8102e" stroke-width="1.6"/></svg>
      <svg viewBox="0 0 15 10" aria-label="Dutch"><rect width="15" height="10" fill="#fff"/><rect width="15" height="3.3" fill="#ae1c28"/><rect y="6.7" width="15" height="3.3" fill="#21468b"/></svg>
      <svg viewBox="0 0 15 10" aria-label="French"><rect width="15" height="10" fill="#fff"/><rect width="5" height="10" fill="#1f3c8a"/><rect x="10" width="5" height="10" fill="#e02b2b"/></svg>
      <svg viewBox="0 0 15 10" aria-label="Italian"><rect width="15" height="10" fill="#fff"/><rect width="5" height="10" fill="#159447"/><rect x="10" width="5" height="10" fill="#d62b2b"/></svg>
    </div>
    <nav class="main-nav">
      <a href="#">Home</a><a href="#">About</a><a href="#">Talent</a><a href="#">Companies</a><a href="#" class="is-active">Jobs</a><a href="#">Events</a><a href="#">Contact</a>
    </nav>
  </header>

  <section class="page-banner">
    <div class="banner-photo" role="img" aria-label="Photo of business people shaking hands"></div>
    <h1 class="banner-title">AVAILABLE JOBS</h1>
    <p class="banner-sub">The right place for choosing a career</p>
  </section>

  <main class="jobs-panel">
    <div class="table-controls">
      <div>Show <span class="entries-select">10</span> Entries</div>
      <div>Search <span class="search-field"></span></div>
    </div>
    <table class="jobs-table">
      <thead><tr><th style="width:80px">NO.</th><th style="width:135px">JOB ID</th><th style="width:240px">POSITION</th><th style="width:150px">LOCATION</th><th>TYPE</th></tr></thead>
      <tbody>
        <tr><td>1</td><td>TN2014001</td><td>Marketing Coordinator</td><td>Zurich</td><td>Temporary</td></tr>
        <tr><td>2</td><td>TN2014002</td><td>Store Manager</td><td>Bern</td><td>Permanent</td></tr>
        <tr><td>3</td><td>TN2014003</td><td>Administration</td><td>Zurich</td><td>Permanent</td></tr>
        <tr><td>4</td><td>TN2014004</td><td>Vice President</td><td>Zurich</td><td>Temporary</td></tr>
        <tr><td>5</td><td>TN2014005</td><td>Technical Engineer</td><td>Zurich</td><td>Permanent</td></tr>
        <tr><td>6</td><td>TN2014006</td><td>IT Manager</td><td>Zurich</td><td>Permanent</td></tr>
        <tr><td>7</td><td>TN2014007</td><td>Database Administrator</td><td>Bern</td><td>Permanent</td></tr>
        <tr class="is-hovered"><td>8</td><td>TN2014008</td><td>Graphic Designer</td><td>Zurich</td><td>Temporary</td></tr>
        <tr><td>9</td><td>TN2014009</td><td>Security</td><td>Zurich</td><td>Temporary</td></tr>
        <tr><td>10</td><td>TN20140010</td><td>Office Boy</td><td>Bern</td><td>Temporary</td></tr>
      </tbody>
    </table>
    <div class="table-info">Showing 1 to 10 of 200 entries</div>
    <div class="pagination"><span>&lt; Previous</span><span>Next &gt;</span></div>
  </main>

  <section class="site-footer-panel">
    <div class="footer-col col-about">
      <h2>ABOUT US</h2>
      <p>Our recruitment website "Crestline Circle" will be focusing on: "Bridging People &amp; Employers in Switzerland"; which means our target audience is two-folded: TALENT &amp; COMPANIES - that are looking for talent for specific job vacancies in Switzerland.</p>
      <span class="more" style="top:170px">:: more details</span>
    </div>
    <div class="footer-divider"></div>
    <div class="footer-col col-jobs">
      <h2>JOBS</h2>
      <p>Trainees for Specialized Technical Trainee Program<br>09/04/2014</p>
      <p>Marketing Coordinator<br>28/03/2014</p>
      <span class="more" style="top:172px">:: more available jobs</span>
    </div>
    <div class="footer-col col-news">
      <h2>NEWS</h2>
      <p>Return of the mega-merger as Norvale and Bexton turn cement into profits<br>09/04/2014</p>
      <p>Swiss startups get help with US market breakthrough<br>28/03/2014</p>
      <span class="more" style="top:172px">:: more news</span>
    </div>
  </section>

  <footer class="site-bottom">
    <p>Copyright 2014 crestlinecircle.ch. All Rights Reserved.</p>
    <p>Terms &amp; Conditions | Disclaimer</p>
  </footer>
  <div class="social-links" aria-label="Social links">
    <span style="background:#5fc4e4"></span><span style="background:#3b5a9a"></span><span style="background:#1a7ab8"></span><span style="background:#c9d82a"></span>
  </div>
  <div class="footer-brand"><span class="brand-mark"></span><span class="name">Crestline Circle</span></div>
</body>
</html>
```